Building Company Business Card Design

I am looking to get a business card designed for my Building Company. Please find the logo attached.

Industry/Entity Type

Business

Contact Information for Business Card

Mobile 0472 913 046
Email admin@tarrowconstructworks.com.au
Website www.tarrowconstructworks.com.au

Colors
0255a3

```html
<!DOCTYPE html>
<html lang="en">
<head>
<meta charset="utf-8">
<title>Tarrow Construct Works – Business Card</title>
<link href="https://fonts.googleapis.com/css2?family=Questrial&display=swap" rel="stylesheet">
<style>
  :root {
    --brand-blue: #0255a3;
    --deep-blue: #0a4a94;
    --accent-grey: #7a7c80;
    --text-grey: #55585c;
    --card-light: #f7f7f7;
    --card-shade: #e6e7e8;
    --backdrop: #3a3b3d;
  }
  * { margin: 0; padding: 0; box-sizing: border-box; }
  html, body { width: 1200px; height: 834px; overflow: hidden; }
  body {
    background: var(--backdrop);
    font-family: "Questrial", "Century Gothic", sans-serif;
    position: relative;
  }
  .card {
    position: absolute;
    width: 540px;
    height: 309px;
    background: linear-gradient(135deg, var(--card-light) 0%, var(--card-shade) 100%);
    overflow: hidden;
    box-shadow: 0 10px 30px rgba(0,0,0,0.45);
  }
  .card--front { left: 40px; top: 262px; }
  .card--back { left: 620px; top: 262px; }
  .card__swoosh { position: absolute; inset: 0; width: 100%; height: 100%; }
  .wordmark {
    position: absolute;
    color: var(--brand-blue);
    font-size: 24px;
    letter-spacing: 1px;
    line-height: 1.05;
    text-transform: uppercase;
  }
  .card--front .wordmark { left: 0; right: 0; top: 92px; text-align: center; }
  .card--back .wordmark { left: 40px; top: 150px; font-size: 20px; }
  .contact {
    position: absolute;
    left: 236px;
    top: 64px;
    color: var(--text-grey);
  }
  .contact__name { font-size: 19px; color: var(--text-grey); }
  .contact__role { font-size: 14px; color: var(--brand-blue); margin-bottom: 14px; }
  .contact__list { list-style: none; font-size: 11.5px; }
  .contact__item { display: flex; align-items: center; gap: 9px; margin-bottom: 6px; }
  .contact__icon { width: 11px; height: 11px; flex: none; }
</style>
</head>
<body>
  <section class="card card--front" aria-label="Card front">
    <svg class="card__swoosh" viewBox="0 0 540 309" preserveAspectRatio="none" aria-hidden="true">
      <path d="M0,285 Q320,300 540,120 L540,309 L0,309 Z" fill="var(--brand-blue)"/>
      <path d="M0,276 Q320,288 540,100" fill="none" stroke="var(--accent-grey)" stroke-width="4"/>
    </svg>
    <div class="wordmark">Tarrow Construct Works</div>
  </section>

  <section class="card card--back" aria-label="Card back">
    <svg class="card__swoosh" viewBox="0 0 540 309" preserveAspectRatio="none" aria-hidden="true">
      <path d="M440,0 Q530,130 520,309 L540,309 L540,0 Z" fill="var(--deep-blue)"/>
      <path d="M408,0 Q510,130 500,309" fill="none" stroke="var(--accent-grey)" stroke-width="4"/>
    </svg>
    <div class="wordmark">Tarrow<br>Construct Works</div>
    <div class="contact">
      <div class="contact__name">Liam Carver</div>
      <div class="contact__role">President</div>
      <ul class="contact__list">
        <li class="contact__item">
          <svg class="contact__icon" viewBox="0 0 12 12" aria-hidden="true"><path d="M1,4 Q6,0 11,4 L9,5 L8,4 L4,4 L3,5 Z M3,6 L9,6 L10,11 L2,11 Z" fill="var(--brand-blue)"/></svg>
          0472 913 046
        </li>
        <li class="contact__item">
          <svg class="contact__icon" viewBox="0 0 12 12" aria-hidden="true"><rect x="1" y="2.5" width="10" height="7" fill="none" stroke="var(--brand-blue)" stroke-width="1.3"/><path d="M1,2.5 L6,7 L11,2.5" fill="none" stroke="var(--brand-blue)" stroke-width="1.3"/></svg>
          admin@tarrowconstructworks.com.au
        </li>
        <li class="contact__item">
          <svg class="contact__icon" viewBox="0 0 12 12" aria-hidden="true"><circle cx="6" cy="6" r="5" fill="none" stroke="var(--brand-blue)" stroke-width="1.2"/><ellipse cx="6" cy="6" rx="2.2" ry="5" fill="none" stroke="var(--brand-blue)" stroke-width="1"/><path d="M1,6 H11" stroke="var(--brand-blue)" stroke-width="1"/></svg>
          www.tarrowconstructworks.com.au
        </li>
      </ul>
    </div>
  </section>
</body>
</html>
```